Harbor Bean Corp Business Card Design

Harbor Bean Corp is a local owner and operator of several coffee shops in Irving, TX. Google "Brew Bright Corner" for an example of one of our shops.We would like an image that is professional, but with a slight nod to the protestant religious nature of our backers.The name "Harbor Bean" is a play on the concept of "rivers of living water". It also conveys the concept of a "life of coffee". We desire to combine these concepts in the logo visualization, with the emphasis on the commercial side of the concept.

Target Market(s)

Upper class retail. No drive-through. Comfy lounges.

Industry/Entity Type

Coffee Shop

Contact Information for Business Card

Dale Mercer
Chief Operating Officer
Harbor Bean Corp
(832) 555 0147
dale@harborbean.example (address not yet active)

Requirements
Must have
• We do not have a logo yet. Need that as a part of the design.
• This needs to be original artwork. I need to own the art when the design is finished. I will look at submissions with stock artwork, but be advised that I will not accept the submission until original work is presented.

```html
<!DOCTYPE html>
<html lang="en">
<head>
<meta charset="utf-8">
<title>Harbor Bean Corp Business Card</title>
<link href="https://fonts.googleapis.com/css2?family=Fredoka:wght@600;700&family=Open+Sans:wght@400;600&display=swap" rel="stylesheet">
<style>
  :root {
    --backdrop: #e6e4dc;
    --olive-dark: #4a472b;
    --olive-mid: #8c8a3c;
    --olive-light: #c9c75c;
    --lime: #dcdb6c;
    --cream: #fbf6dc;
    --ink: #3e3526;
  }
  * { margin: 0; padding: 0; box-sizing: border-box; }
  html, body {
    width: 1200px; height: 1034px; overflow: hidden;
    background: var(--backdrop);
  }
  .stage {
    position: relative; width: 1200px; height: 1034px;
  }
  .card {
    position: absolute; top: 167px;
    width: 400px; height: 700px; overflow: hidden;
    box-shadow: 0 6px 18px rgba(0,0,0,0.18);
  }
  .card--front { left: 170px; }
  .card--back { left: 630px; }
  .card__bg { position: absolute; inset: 0; width: 100%; height: 100%; }
  .sunburst {
    position: absolute; inset: 0;
    background: radial-gradient(circle at 50% 42%, #9c9a45 0%, #6e6b36 45%, var(--olive-dark) 100%);
  }
  .brand {
    position: absolute; left: 0; right: 0;
    display: flex; flex-direction: column; align-items: center; gap: 14px;
  }
  .card--front .brand { top: 200px; }
  .card--back .brand { top: 110px; }
  .brand__dot {
    width: 130px; height: 130px; border-radius: 50%;
    background: var(--cream);
  }
  .brand__name {
    font-family: "Fredoka", sans-serif; font-weight: 700;
    font-size: 34px; color: var(--cream); letter-spacing: 0.5px;
  }
  .person {
    position: absolute; left: 0; right: 0; top: 430px; text-align: center;
    font-family: "Fredoka", sans-serif; font-weight: 700; text-transform: uppercase;
  }
  .person__name { font-size: 36px; color: var(--ink); letter-spacing: 1px; }
  .person__name .surname { color: var(--cream); }
  .person__title { font-size: 15px; color: var(--ink); letter-spacing: 1px; margin-top: 2px; }
  .contact__phone {
    position: absolute; left: 55px; top: 560px;
    width: 290px; height: 62px; border-radius: 10px;
    background: var(--ink); color: var(--cream);
    font-family: "Open Sans", sans-serif; font-weight: 600; font-size: 31px;
    display: flex; align-items: center; justify-content: center;
  }
  .contact__email {
    position: absolute; left: 0; right: 0; top: 632px; text-align: center;
    font-family: "Open Sans", sans-serif; font-size: 15px; color: var(--ink);
  }
</style>
</head>
<body>
<main class="stage">
  <section class="card card--front">
    <div class="sunburst" role="img" aria-label="Swirling olive sunburst stripe pattern"></div>
    <div class="brand">
      <span class="brand__dot"></span>
      <span class="brand__name">Harbor Bean Corp</span>
    </div>
  </section>

  <section class="card card--back">
    <svg class="card__bg" viewBox="0 0 400 700" preserveAspectRatio="none" aria-hidden="true">
      <rect width="400" height="700" fill="var(--olive-light)"/>
      <polygon points="0,0 400,0 400,330 0,110" fill="var(--olive-dark)"/>
      <polygon points="0,110 400,330 400,470 0,250" fill="var(--olive-mid)"/>
      <polygon points="0,560 400,700 0,700" fill="var(--lime)"/>
    </svg>
    <div class="brand">
      <span class="brand__dot"></span>
      <span class="brand__name">Harbor Bean Corp</span>
    </div>
    <div class="person">
      <p class="person__name">Dale <span class="surname">Mercer</span></p>
      <p class="person__title">Chief Operating Officer</p>
    </div>
    <p class="contact__phone">(832) 555 0147</p>
    <p class="contact__email">dale@harborbean.example</p>
  </section>
</main>
</body>
</html>
```